Flyer for Fundraising Marathon Run for a Charity

Hi. I am running the distance of a marathon race to solicit donations for a charitable cause. I need a well designed flyer to help me solicit support from friends and others. The copy for the flyer is attached. There is a significant amount of written text so it will need to be laid out in a way that is easy to read but also mixes well with some good images and design appeal. I am open to creative ideas. I’ve attached a photo of me from the last time I ran this charity marathon run, the area in Delphi where I will be running and the information for the flyer. These photos don't have to be used if there are animation or drawings that might work with creative appeal. Otherwise, I am open to other stock photos or graphics. Feel free to contact me if you have questions. Thank you !

Industry/Entity Type

Charity

Requirements
Must have
• 8.5 X 11 inches in size

```html
<!DOCTYPE html>
<html lang="en">
<head>
<meta charset="utf-8">
<title>Prayer Run Fundraiser Flyer</title>
<link rel="stylesheet" href="https://fonts.googleapis.com/css2?family=Oswald:wght@400;500&family=Barlow+Condensed:wght@500&display=swap">
<style>
  :root {
    --sky-top: #86daf4;
    --sky-bottom: #02a3d9;
    --swoosh: #b8ecfb;
    --navy: #15245a;
    --white: #ffffff;
    --band: #eaf8fd;
    --landscape-a: #3a6fb0;
    --landscape-b: #8a7a5e;
    --portrait-a: #6f8a5a;
    --portrait-b: #b3243a;
  }
  * { margin: 0; padding: 0; box-sizing: border-box; }
  html, body { width: 850px; height: 1200px; overflow: hidden; background: var(--white); }
  .flyer {
    position: relative;
    width: 850px; height: 1200px; overflow: hidden;
    background: linear-gradient(180deg, var(--sky-top) 0%, #4cc3ec 45%, var(--sky-bottom) 100%);
    font-family: "Barlow Condensed", "Arial Narrow", sans-serif;
    font-weight: 500;
    color: var(--navy);
  }
  .shapes { position: absolute; inset: 0; }
  .tagline {
    position: absolute; top: 12px; left: 0; width: 850px;
    text-align: center;
    font-family: "Oswald", "Arial Narrow", sans-serif;
    font-size: 31px; color: var(--white); letter-spacing: 0.2px;
  }
  .headline {
    position: absolute; top: 166px; left: 20px; width: 820px;
    text-align: center;
    font-family: "Oswald", "Arial Narrow", sans-serif;
    font-weight: 500;
    font-size: 47px; line-height: 52px; color: var(--white);
    text-shadow: 2px 2px 3px rgba(0,0,0,0.55);
  }
  .copy {
    position: absolute; right: 30px;
    text-align: right; font-size: 19.5px; line-height: 25.6px;
  }
  .copy--intro { top: 309px; width: 720px; }
  .copy--sponsor { top: 393px; width: 660px; }
  .copy--link { display: block; color: var(--white); font-size: 21px; }
  .copy--concept { top: 534px; width: 520px; }
  .copy--question { top: 718px; width: 520px; font-size: 17px; line-height: 19px; }
  .steps { position: absolute; right: 30px; width: 520px; text-align: right; list-style: none; font-size: 16.5px; line-height: 19.5px; }
  .step-1 { top: 778px; }
  .step-2 { top: 817px; }
  .step-3 { top: 855px; }
  .step-4 { top: 913px; }
  .step-5 { top: 1030px; }
</style>
</head>
<body>
<div class="flyer">
  <svg class="shapes" width="850" height="1200" viewBox="0 0 850 1200">
    <defs>
      <linearGradient id="landscapeTone" x1="0" y1="0" x2="0" y2="1">
        <stop offset="0" stop-color="var(--landscape-a)"/>
        <stop offset="0.5" stop-color="#5d86b8"/>
        <stop offset="1" stop-color="var(--landscape-b)"/>
      </linearGradient>
      <linearGradient id="portraitTone" x1="0" y1="0" x2="1" y2="1">
        <stop offset="0" stop-color="var(--portrait-a)"/>
        <stop offset="0.6" stop-color="#8c6b55"/>
        <stop offset="1" stop-color="var(--portrait-b)"/>
      </linearGradient>
    </defs>

    <!-- light swoosh band -->
    <path d="M120 90 C40 110 10 200 30 300 C60 420 230 440 300 560 C370 700 250 960 280 1200 L180 1200 C170 960 290 720 230 580 C170 450 0 420 0 300 L0 150 C20 110 70 95 120 90 Z" fill="var(--swoosh)" opacity="0.85"/>

    <!-- landscape banner -->
    <path role="img" aria-label="Photo of the Delphi coastline with hills, bay and olive groves" d="M80 90 L850 90 L850 296 L30 296 C24 200 40 120 80 90 Z" fill="url(#landscapeTone)"/>

    <!-- top border band -->
    <rect x="80" y="94" width="770" height="24" fill="var(--band)" opacity="0.9"/>

    <!-- portrait area -->
    <path role="img" aria-label="Photo of the runner in a red top covered with coloured prayer ribbons" d="M12 436 C110 470 230 500 260 600 C285 700 220 900 232 1140 L12 1140 Z" fill="url(#portraitTone)"/>

    <!-- faint runner figures -->
    <rect role="img" aria-label="Faint runner silhouettes" x="170" y="478" width="132" height="96" rx="10" fill="var(--white)" opacity="0.35"/>

    <!-- bottom border band -->
    <rect x="152" y="1146" width="668" height="36" fill="var(--band)" opacity="0.9"/>
  </svg>

  <p class="tagline">Your Prayer Can Make A Difference For You &amp; For A Good Cause !</p>

  <h1 class="headline">A Special Journey For Your Specific Prayers<br>&amp; For An Important Ancient Cause</h1>

  <p class="copy copy--intro">This coming April 22 2017 Dean Halloway will make a special running journey of 26 miles through the ancient lands of Apollo and Athena at Delphi on Mt. Parnassus in Greece.</p>

  <p class="copy copy--sponsor">Dean will adorn his running outfit with special cloth strips that will contain written prayers and petitions of people who will sponsor his journey by making a charitable donation to the Parnassian Heritage Union, an organization that preserves the land and the Delphic culture.<span class="copy--link">www.parnassian-heritage-union.org</span></p>

  <p class="copy copy--concept">The concept is simple and very powerful: as Dean runs, your written prayer on a cloth strip will flow and emanate in the wind – being blessed by the spirits of this ancient and magical land – asking unto the wind that your prayer be answered.&nbsp; This type of prayer practice dates back to ancient times.&nbsp; The Tibetan culture commonly uses prayer flags with special mantras and symbols.</p>

  <p class="copy copy--question">Will you make a prayer for yourself or a loved and support a good cause? Here is how to get your prayer started:</p>

  <ol class="steps-list">
    <li class="steps step-1">1) Decide what you want your prayer, petition or intention to be.</li>
    <li class="steps step-2">2) Define your prayer, petition or intention by writing it down.</li>
    <li class="steps step-3">3) Refine it is concise, clear &amp; specific. (18 words or less is ideal for each strip cloth).</li>
    <li class="steps step-4">4) Contact Dean at dhalloway@hallowayreed.com and tell him how many prayer cloth strips you wish to obtain. Dean will then send you the cloth for you to write your prayer and send back to him or he will write out the prayer for you. Dean can also answer any questions you may have.</li>
    <li class="steps step-5">5) A minimum donation of $25 for each prayer cloth is requested. Checks can be made to the “Dean Halloway/Parnassian Heritage Union” and mail to Dean M. Halloway, Halloway Reed PLC, 1480 Harbor Lane, Ste. 204 Ashford, Virginia 23199 or though online payment instructions sent by email from Dean as requested.</li>
  </ol>
</div>
</body>
</html>
```